Web Design Project

We need a web design for a new company. We have a logo, and we've identified the style of a website that we'd like to adapt (www.tovendrafield.example). We do not sell to the public. The purpose of the site is (1) to allow our appointed sales partners to log in to our proprietary database system and (2) to provide a basic web presence and some basic information about our company.

We sell business insurance through independent agents - our sales partners.

Please do not use a photo of a person/s as a central design element, or at all.

Target Market(s)

The purpose of the site is not to sell, but to provide a professional landing page for a log in and some basic company information.

Industry/Entity Type

Business

Requirements
Must have
• A professional look. Agent log in must be central, clear and easy. Use of our logo and our colors.
Should not have
• Photos of people

```html
<!DOCTYPE html>
<html lang="en">
<head>
<meta charset="utf-8">
<title>Northbank Insurance</title>
<link href="https://fonts.googleapis.com/css2?family=PT+Sans:ital,wght@0,400;0,700;1,400&family=PT+Sans+Narrow:wght@400;700&display=swap" rel="stylesheet">
<style>
  :root {
    --navy-deep: #0b1c2a;
    --header-band: #13293a;
    --hero-top: #1d4d6e;
    --hero-mid: #2a6b93;
    --hero-glow: #4aa3cf;
    --accent: #3ec0e6;
    --accent-btn: #33b5e0;
    --text-light: #e9f3f8;
    --login-band: #ececec;
    --label-blue: #3b6a8e;
    --card-head: #0a1620;
    --body-text: #6b6b6b;
    --title-text: #2d2d2d;
    --rule: #d6d6d6;
    --footer: #3a3a3a;
    --footer-top: #2a2a2a;
  }
  * { box-sizing: border-box; margin: 0; padding: 0; }
  html, body { width: 1200px; height: 1029px; overflow: hidden; background: #fff; }
  body { position: relative; font-family: "PT Sans Narrow", "Arial Narrow", sans-serif; }

  .hero {
    position: absolute; left: 0; top: 0; width: 1200px; height: 463px;
    background: radial-gradient(ellipse 420px 260px at 380px 250px, var(--hero-glow) 0%, var(--hero-mid) 45%, var(--hero-top) 100%);
  }
  .header-band {
    position: absolute; left: 0; top: 24px; width: 1200px; height: 61px;
    background: repeating-linear-gradient(135deg, var(--header-band) 0 2px, #10232f 2px 4px);
  }
  .brand {
    position: absolute; left: 197px; top: 24px; height: 61px;
    display: flex; align-items: center; gap: 10px;
    font-family: "PT Sans", sans-serif; font-weight: 700; font-size: 20px;
    color: #ffffff; letter-spacing: .5px;
  }
  .brand-mark { width: 16px; height: 16px; background: var(--accent); }
  .main-nav { position: absolute; top: 24px; height: 61px; left: 0; width: 1200px; }
  .main-nav a {
    position: absolute; top: 0; line-height: 61px; transform: translateX(-50%);
    font-family: "PT Sans Narrow", sans-serif; font-weight: 700; font-size: 13px;
    letter-spacing: 1px; color: var(--accent); text-decoration: none;
  }
  .main-nav a.active { color: #fff; }

  .skyline {
    position: absolute; left: 176px; top: 163px; width: 441px; height: 231px;
    background: linear-gradient(180deg, rgba(74,163,207,.15) 0%, #0e2535 55%, rgba(46,111,150,.5) 100%);
  }
  .hero-copy { position: absolute; left: 666px; top: 158px; width: 354px; }
  .hero-copy h1 {
    font-family: "PT Sans", sans-serif; font-weight: 400; font-size: 31px; line-height: 36px;
    color: var(--accent); letter-spacing: .5px;
  }
  .hero-copy h1 span { display: block; color: #fff; }
  .hero-copy h2 {
    margin-top: 4px; font-family: "PT Sans", sans-serif; font-weight: 400; font-size: 17px;
    color: var(--accent); padding-bottour: 0; padding-bottom: 9px;
    border-bottom: 1px dotted rgba(140,200,230,.6);
  }
  .hero-copy p { margin-top: 9px; font-size: 13px; line-height: 19px; color: var(--text-light); }
  .btn-primary {
    display: inline-block; margin-top: 17px; width: 84px; height: 33px; line-height: 33px;
    text-align: center; background: var(--accent-btn); color: #fff; font-size: 13.5px;
    text-decoration: none;
  }

  .login-band {
    position: absolute; left: 0; top: 463px; width: 1200px; height: 64px;
    background: var(--login-band); border-bottom: 1px solid #d8d8d8;
  }
  .login-band label {
    position: absolute; top: 25px; font-family: "PT Sans", sans-serif; font-style: italic;
    font-size: 12.5px; letter-spacing: 1px; color: var(--label-blue);
  }
  .login-band .field {
    position: absolute; top: 18px; height: 28px; background: #fff; border: 1px solid #cfcfcf;
  }
  .go-btn {
    position: absolute; left: 792px; top: 18px; width: 28px; height: 28px;
    background: #6aa3cc; display: flex; align-items: center; justify-content: center;
  }
  .divider { position: absolute; left: 847px; top: 17px; height: 30px; border-left: 2px dotted #bdbdbd; }
  .btn-register {
    position: absolute; left: 875px; top: 17px; width: 103px; height: 30px;
    background: linear-gradient(#fff, #eee); border: 1px solid #d3d3d3;
    font-family: "PT Sans", sans-serif; font-size: 12.5px; letter-spacing: 1px;
    color: var(--label-blue); text-align: center; line-height: 28px;
  }

  .card { position: absolute; top: 570px; width: 238px; }
  .card-head {
    height: 32px; line-height: 32px; text-align: center; background: var(--card-head);
    font-family: "PT Sans", sans-serif; font-weight: 700; font-size: 15.5px; color: #fff;
  }
  .card-photo { margin-top: 5px; height: 122px; }
  .photo-tower { background: linear-gradient(160deg, #e8f1f8, #7fa6c9 60%, #c9dceb); }
  .photo-keys { background: linear-gradient(150deg, #2b2b2b, #5a5a5a 50%, #6d8fa8 55%, #333); }
  .photo-form { background: linear-gradient(160deg, #cfdff0, #f2f6fb 50%, #b9cfe6); }
  .card h3 {
    margin-top: 13px; padding: 6px 0 5px; border-top: 1px solid var(--rule); border-bottom: 1px solid var(--rule);
    font-family: "PT Sans", sans-serif; font-weight: 400; font-size: 17px; letter-spacing: .5px; color: var(--title-text);
  }
  .card p { margin-top: 10px; font-size: 13px; line-height: 20.5px; color: var(--body-text); }
  .more-link {
    display: inline-flex; align-items: center; gap: 6px; margin-top: 14px;
    font-size: 13px; color: var(--accent); text-decoration: none;
  }

  .site-footer {
    position: absolute; left: 0; top: 956px; width: 1200px; height: 73px;
    border-top: 5px solid var(--footer-top);
    background: repeating-linear-gradient(135deg, var(--footer) 0 2px, #444 2px 4px);
    font-size: 12.5px; color: #fff;
  }
  .site-footer .copy { position: absolute; left: 171px; top: 28px; }
  .site-footer a { position: absolute; top: 28px; color: #fff; text-decoration: none; }
  .site-footer a.current { color: var(--accent); }
</style>
</head>
<body>
  <section class="hero">
    <div class="header-band"></div>
    <div class="brand"><span class="brand-mark"></span>Northbank Insurance</div>
    <nav class="main-nav">
      <a class="active" href="#" style="left:596px">HOME</a>
      <a href="#" style="left:668px">ABOUT</a>
      <a href="#" style="left:745px">SERVICES</a>
      <a href="#" style="left:831px">OUR WORK</a>
      <a href="#" style="left:911px">BLOG</a>
      <a href="#" style="left:981px">CONTACT</a>
    </nav>
    <div class="skyline" role="img" aria-label="City skyline silhouette reflected in water against a glowing blue sky"></div>
    <div class="hero-copy">
      <h1>Sungelle Molestielle<span>Fore Refed Berreferid</span></h1>
      <h2>Proin vehicula pulvinar nisi ac semper</h2>
      <p>Lorem ipsum dolor sit amet, consectetur adipiscing elit. Praesent dolor nunc, rhoncus porttitor bibendum in, placerat sed dui rae-sent suscipit consequat nunc, et accumsan arcu.</p>
      <a class="btn-primary" href="#">read more</a>
    </div>
  </section>

  <section class="login-band">
    <label style="left:209px">Login User</label>
    <div class="field" style="left:288px; width:211px"></div>
    <label style="left:539px">Password</label>
    <div class="field" style="left:609px; width:211px"></div>
    <div class="go-btn"><svg width="6" height="8" viewBox="0 0 6 8"><path d="M0 0 L6 4 L0 8 Z" fill="#fff"/></svg></div>
    <div class="divider"></div>
    <div class="btn-register">Register</div>
  </section>

  <article class="card" style="left:197px">
    <div class="card-head">Lorem Ipsum</div>
    <div class="card-photo photo-tower" role="img" aria-label="Glass office tower seen from below"></div>
    <h3>Lorem Ipsum Dolor</h3>
    <p>Lorem ipsum dolor sit amet, consectetur adipis ing elit. Praesent dolor nunc, rhoncus portti-torol bibendum in, placerat sed dui raesent suscipiten consequat nunc.</p>
    <a class="more-link" href="#">read more <svg width="12" height="6" viewBox="0 0 12 6"><path d="M0 3 H10 M7 0.5 L11 3 L7 5.5" stroke="#3ec0e6" stroke-width="1.3" fill="none"/></svg></a>
  </article>
  <article class="card" style="left:483px">
    <div class="card-head">Lorem Ipsum</div>
    <div class="card-photo photo-keys" role="img" aria-label="Keyboard with a blue insurance key"></div>
    <h3>Lorem Ipsum Dolor</h3>
    <p>Lorem ipsum dolor sit amet, consectetur adipis ing elit. Praesent dolor nunc, rhoncus portti-torol bibendum in, placerat sed dui raesent suscipiten consequat nunc.</p>
    <a class="more-link" href="#">read more <svg width="12" height="6" viewBox="0 0 12 6"><path d="M0 3 H10 M7 0.5 L11 3 L7 5.5" stroke="#3ec0e6" stroke-width="1.3" fill="none"/></svg></a>
  </article>
  <article class="card" style="left:766px">
    <div class="card-head">Lorem Ipsum</div>
    <div class="card-photo photo-form" role="img" aria-label="Pen resting on an application form"></div>
    <h3>Lorem Ipsum Dolor</h3>
    <p>Lorem ipsum dolor sit amet, consectetur adipis ing elit. Praesent dolor nunc, rhoncus portti-torol bibendum in, placerat sed dui raesent suscipiten consequat nunc.</p>
    <a class="more-link" href="#">read more <svg width="12" height="6" viewBox="0 0 12 6"><path d="M0 3 H10 M7 0.5 L11 3 L7 5.5" stroke="#3ec0e6" stroke-width="1.3" fill="none"/></svg></a>
  </article>

  <footer class="site-footer">
    <div class="copy">Copyright © 2012 &nbsp;|&nbsp; All rights reserved</div>
    <a href="#" style="left:824px">Home</a>
    <a href="#" style="left:883px">About</a>
    <a href="#" style="left:940px">Contact</a>
    <a class="current" href="#" style="left:1004px">Login</a>
  </footer>
</body>
</html>
```